Brochure Design Project

I am looking for a trifold brochure.
I would like it to be square (5.5 x 5.5)
The back needs to be reserved for a map and logo information.

we are a financial planning firm. we have been in operation for 15 years.
our clients are ecstatic and continue to refer others to us.

Brochure COPY:
Building Wealth, Building Futures
We start with your goals. Then we build a comprehensive strategy to manage your investments, grow your wealth, minimize your tax burden and protect your family. Most importantly, we keep you informed about market change, opportunities and concerns before they impact you, so you can make confident decisions about your future, every step of the way.

Understanding and Expertise (bios)
Steadfast Money Partners is led by Marla Tofvenson and Rosalind Pike, experienced business partners who take the time to listen to you, understand your needs and present you with all your options.
Our focus in on your future, and building a confident and financially secure path for you and your family for the years ahead.

Marla Tofvenson, BSc, MBA, CPA, CA, CFP, FMA, CPCA
Certified Financial Planner

With years of experience in tax, investment, estate and retirement issues - and an extensive business background - Marla provided her clients with important financial insights and clear direction in a friendly and open manner.

Rosalind Pike, BSEd, FMA, CPCA, CFP, FCSI, CIM

After a successful tennis career Rosalind joined Marla in the financial industry. Rosalind quickly discovered how much she enjoys working with people and helping them to achieve their goals. Leveraging the discipline and work ethic developed during her tennis career, Rosalind has been instrumental in creating the successful process used by Steadfast Money Partners.

People Trust Us to Help Them
The important things in life are often neglected due to the demands of day to day, including financial planning and wealth management. But it doesn't have to be that way when you have a trustworthy team looking out for you.
At Steadfast Money Partners we have the knowledge, experience and resources to help you move forward and realize your financial goals.

(side note) on the back of the brochure it should have the SMP logo, the office address, 382 Quillbrook Rd. E. Mississauga, ON L5R 7K9, and our website address.

Reason: Am juggling a number of different projects so need to extend the deadline on this one. Will provide copy for the project by end of day today.

Target Market(s)

We would like the brochure to appeal to the high net worth client who is currently working with an advisor but is not getting the attention from them.

Industry/Entity Type

Financial

Requirements
Must have
• SMP Logo on the front. The logo is blue with black font and has a tagline with it that says "Choose your path, change your future."
you can see the logo at www.plotyourmorrow.ca

One page must be about the two advisors, Marla Tofvenson and Rosalind Pike.
(leave an open area for bios and we will fill it in)

We want it to talk about building wealth and passing it on to the next generation.
Should not have
• Financial lingo.

```html
<!DOCTYPE html>
<html lang="en">
<head>
<meta charset="utf-8">
<title>Steadfast Money Partners – Trifold Brochure</title>
<link rel="stylesheet" href="https://fonts.googleapis.com/css2?family=Roboto+Condensed:wght@300;400;700&family=Arimo:wght@400;700&display=swap">
<style>
  :root {
    --canvas: #e6e6e4;
    --charcoal: #4b4c50;
    --charcoal-dark: #3d3e42;
    --slate: #5a5b5f;
    --blue: #1f62ad;
    --blue-deep: #174d8e;
    --blue-light: #e6edf6;
    --paper: #ffffff;
    --ink: #555559;
    --ink-soft: #6f7074;
    --quote: #e9e9e9;
    --photo-warm: #cfc4b8;
    --map-land: #dfe6ee;
    --map-road: #ffffff;
  }
  * { box-sizing: border-box; margin: 0; padding: 0; }
  html, body { width: 1200px; height: 900px; overflow: hidden; }
  body {
    background: var(--canvas);
    font-family: "Arimo", Arial, sans-serif;
    color: var(--ink);
    position: relative;
  }
  .spread {
    position: absolute;
    left: 30px;
    width: 1140px;
    height: 380px;
    display: flex;
    box-shadow: 0 4px 14px rgba(0,0,0,0.18);
  }
  .spread--outside { top: 45px; }
  .spread--inside { top: 475px; }
  .panel { width: 380px; height: 380px; position: relative; overflow: hidden; }

  /* Outside: quote panel */
  .panel--quote {
    background: linear-gradient(90deg, var(--charcoal-dark), var(--charcoal));
    padding: 26px 28px;
  }
  .quote-text {
    font-family: "Roboto Condensed", "Arial Narrow", sans-serif;
    font-weight: 400;
    font-size: 50px;
    line-height: 1.04;
    color: var(--quote);
    letter-spacing: -0.5px;
  }
  .quote-author {
    font-family: "Roboto Condensed", sans-serif;
    font-weight: 700;
    font-size: 14px;
    color: #b9babd;
    margin-left: 10px;
    letter-spacing: 0;
  }

  /* Outside: back panel with contact and map */
  .panel--contact {
    background: linear-gradient(180deg, var(--blue) 0%, var(--blue-deep) 100%);
    color: #fff;
    padding: 26px 22px;
  }
  .thumb-row { display: flex; gap: 8px; }
  .thumb {
    width: 46px; height: 46px;
    border: 2px solid #fff;
    background: linear-gradient(135deg, var(--photo-warm), #b59c86);
  }
  .thumb:nth-child(2) { background: linear-gradient(135deg, #e0c7a8, #a98c72); }
  .thumb:nth-child(3) { background: linear-gradient(135deg, #c9d2dc, #8c97a4); }
  .office-map {
    position: absolute; left: 22px; right: 22px; top: 84px; height: 92px;
    background: var(--map-land);
    border: 2px solid #fff;
  }
  .office-map svg { display: block; width: 100%; height: 100%; }
  .contact-block {
    position: absolute; left: 22px; right: 22px; bottom: 16px;
    font-size: 8.5px; line-height: 1.42;
  }
  .contact-heading { font-weight: 700; font-size: 9.5px; margin-bottom: 8px; }
  .contact-firm { font-weight: 700; }
  .contact-web { font-weight: 700; }
  .hours-heading { font-weight: 700; margin-top: 8px; }

  /* Outside: cover */
  .panel--cover { background: var(--paper); }
  .cover-photo {
    position: absolute; left: 18px; top: 0; width: 362px; height: 258px;
    background: linear-gradient(160deg, #d8d2cb 0%, #c7b19c 45%, #8e97a6 100%);
  }
  .brand { position: absolute; right: 22px; bottom: 34px; text-align: right; }
  .brand-line { display: flex; align-items: center; justify-content: flex-end; gap: 8px; }
  .brand-mark { width: 14px; height: 14px; border-radius: 50%; background: var(--blue); }
  .brand-name { font-weight: 400; font-size: 21px; color: var(--ink); }
  .brand-tagline { font-size: 11px; color: var(--blue); margin-top: 3px; }

  /* Inside: about */
  .panel--about { background: var(--paper); padding: 16px 20px; }
  .label { font-size: 8.5px; font-weight: 700; color: var(--blue); margin-bottom: 4px; }
  .body-copy { font-size: 7px; line-height: 1.45; color: var(--ink-soft); }
  .section-title {
    font-family: "Roboto Condensed", sans-serif;
    font-weight: 700;
    font-size: 17px;
    color: var(--blue);
    margin: 12px 0 8px;
  }
  .advisor {
    display: flex; gap: 10px;
    background: var(--blue-light);
    border-top: 3px solid var(--blue);
    padding: 7px 8px;
    margin-bottom: 9px;
  }
  .advisor-photo {
    flex: 0 0 54px; height: 66px;
    background: linear-gradient(160deg, #cfd3d8, #8f959d);
  }
  .advisor-name { font-size: 10px; font-weight: 700; color: var(--blue); }
  .advisor-credentials { font-size: 6.5px; font-weight: 700; color: var(--ink); margin: 1px 0 3px; }

  /* Inside: services */
  .panel--services { background: var(--paper); padding: 16px 20px; border-left: 1px solid #e2e2e2; }
  .services-label { margin-top: 10px; }
  .service-list { width: 104px; }
  .service { margin-bottom: 8px; }
  .service-name { font-size: 7.5px; font-weight: 700; color: var(--blue); }
  .services-photo {
    position: absolute; left: 134px; top: 136px; width: 246px; height: 244px;
    background: linear-gradient(170deg, #f4f4f4 0%, #e2dcd4 40%, #b9a897 100%);
  }

  /* Inside: testimonials */
  .panel--testimonials { background: var(--slate); padding: 20px 22px; }
  .panel--testimonials .label { color: #fff; }
  .testimonial { margin-top: 14px; }
  .testimonial-text {
    font-family: "Roboto Condensed", sans-serif;
    font-weight: 300;
    font-size: 15.5px;
    line-height: 1.25;
    color: #f1f1f1;
  }
  .testimonial-author { text-align: right; font-size: 8.5px; font-weight: 700; color: #fff; margin-top: 3px; }
</style>
</head>
<body>

<section class="spread spread--outside">
  <div class="panel panel--quote">
    <p class="quote-text">“What one generation sees as a luxury, the next sees as a necessity.”<span class="quote-author">Dorsey, Malcolm</span></p>
  </div>

  <div class="panel panel--contact">
    <div class="thumb-row">
      <div class="thumb" role="img" aria-label="Photo of a smiling family"></div>
      <div class="thumb" role="img" aria-label="Photo of parents with children"></div>
      <div class="thumb" role="img" aria-label="Photo of a family meeting an advisor"></div>
    </div>
    <div class="office-map" role="img" aria-label="Map showing the office location on Quillbrook Rd. E., Mississauga">
      <svg viewBox="0 0 332 88" preserveAspectRatio="none" aria-hidden="true">
        <rect width="332" height="88" fill="#dfe6ee"/>
        <path d="M0 52 H332" stroke="#ffffff" stroke-width="6"/>
        <path d="M120 0 V88" stroke="#ffffff" stroke-width="4"/>
        <path d="M250 0 L230 88" stroke="#ffffff" stroke-width="3"/>
        <circle cx="170" cy="40" r="6" fill="#1f62ad"/>
        <circle cx="170" cy="40" r="2.2" fill="#ffffff"/>
      </svg>
    </div>
    <div class="contact-block">
      <p class="contact-heading">Contact Details</p>
      <p class="contact-firm">Steadfast Money Partners</p>
      <p>Northvale Securities Incorporated</p>
      <p>Northvale Securities Insurance Inc.</p>
      <p>382 Quillbrook Rd. E. Mississauga, ON L5R 7K9</p>
      <p>Telephone: 905-555-0142 &nbsp;·&nbsp; Toll Free: 1-866-555-0187</p>
      <p>Fax: 905-555-0163</p>
      <p class="contact-web">www.plotyourmorrow.ca</p>
      <p class="hours-heading">Hours of Business</p>
      <p>Our business hours are Monday thru Friday from 9am to 5pm. After hour appointments can be scheduled.</p>
    </div>
  </div>

  <div class="panel panel--cover">
    <div class="cover-photo" role="img" aria-label="Photo of three generations of a smiling family"></div>
    <div class="brand">
      <div class="brand-line">
        <span class="brand-mark"></span>
        <span class="brand-name">Steadfast Money Partners</span>
      </div>
      <p class="brand-tagline">Choose your path, change your future.</p>
    </div>
  </div>
</section>

<section class="spread spread--inside">
  <div class="panel panel--about">
    <p class="label">Building Wealth, Building Futures</p>
    <p class="body-copy">We start with your goals. Then we build a comprehensive strategy to manage your investments, grow your wealth, minimize your tax burden and protect your family. Most importantly, we keep you informed about market change, opportunities and concerns before they impact you, so you can make confident decisions about your future, every step of the way.</p>
    <h2 class="section-title">Meet Your Dedicated Wealth Managers</h2>
    <div class="advisor">
      <div class="advisor-photo" role="img" aria-label="Portrait of Marla Tofvenson"></div>
      <div>
        <p class="advisor-name">Marla Tofvenson</p>
        <p class="advisor-credentials">BSc, MBA, CPA, CA, CFP, FMA, CPCA · Certified Financial Planner</p>
        <p class="body-copy">With years of experience in tax, investment, estate and retirement issues - and an extensive business background - Marla provides her clients with important financial insights and clear direction in a friendly and open manner.</p>
      </div>
    </div>
    <div class="advisor">
      <div class="advisor-photo" role="img" aria-label="Portrait of Rosalind Pike"></div>
      <div>
        <p class="advisor-name">Rosalind Pike</p>
        <p class="advisor-credentials">BSEd, FMA, CPCA, CFP, FCSI, CIM</p>
        <p class="body-copy">After a successful tennis career Rosalind joined Marla in the financial industry. Rosalind quickly discovered how much she enjoys working with people and helping them to achieve their goals. Leveraging the discipline and work ethic developed during her tennis career, Rosalind has been instrumental in creating the successful process used by Steadfast Money Partners.</p>
      </div>
    </div>
  </div>

  <div class="panel panel--services">
    <p class="label">People Trust Us to Help Them</p>
    <p class="body-copy">The important things in life are often neglected due to the demands of day to day, including financial planning and wealth management. But it doesn't have to be that way when you have a trustworthy team looking out for you. At Steadfast Money Partners we have the knowledge, experience and resources to help you move forward and realize your financial goals.</p>
    <p class="label services-label">Our Services</p>
    <div class="service-list">
      <div class="service">
        <p class="service-name">Manage Investments</p>
        <p class="body-copy">Steady, clear care for the money you have built.</p>
      </div>
      <div class="service">
        <p class="service-name">Grow Your Wealth</p>
        <p class="body-copy">A plan that builds on your goals, year after year.</p>
      </div>
      <div class="service">
        <p class="service-name">Lower Your Taxes</p>
        <p class="body-copy">Keep more of what you earn, now and later.</p>
      </div>
      <div class="service">
        <p class="service-name">Protect Your Family</p>
        <p class="body-copy">Pass your wealth on to the next generation with care.</p>
      </div>
    </div>
    <div class="services-photo" role="img" aria-label="Photo of a joyful family jumping together"></div>
  </div>

  <div class="panel panel--testimonials">
    <p class="label">Testimonials</p>
    <div class="testimonial">
      <p class="testimonial-text">“They listened first, then built a plan around our family. For the first time we know exactly where our money is going and why.”</p>
      <p class="testimonial-author">Client since 2011</p>
    </div>
    <div class="testimonial">
      <p class="testimonial-text">“Our old advisor rarely called. Here we hear about changes before they matter, and every decision feels like our own.”</p>
      <p class="testimonial-author">Client since 2015</p>
    </div>
    <div class="testimonial">
      <p class="testimonial-text">“We are passing real wealth on to our children now, with a clear plan we all understand and trust.”</p>
      <p class="testimonial-author">Client since 2008</p>
    </div>
  </div>
</section>

</body>
</html>
```